Website Redesign: I want it to look more modern and be easier to read and use.

My current website is www.coinharborly.com. I want my website redesigned to look more modern and user friendly. Something more like these websites-

tellobudgetry.com
https://www.rivenfundhouse.com/
https://www.quarmoly.com/

Industry/Entity Type

Financial Technology

Coding

Coded - Design and coding required

Number of Pages Required

1 page

Font styles to use
Other font styles liked:
• Lato or something similar.

Requirements
Nice to have
• Layout should be similar to these websites- tellobudgetry.com https://www.rivenfundhouse.com/ https://www.quarmoly.com/
Should not have
• No animated banner at the top. The banner image should be static.

```html
<!DOCTYPE html>
<html lang="en">
<head>
<meta charset="utf-8">
<title>CoinHarborly – Retirement &amp; Financial Planning Software</title>
<link href="https://fonts.googleapis.com/css2?family=Allura&family=Lato:wght@400;700&family=Libre+Baskerville:wght@400;700&display=swap" rel="stylesheet">
<style>
:root{
  --navy:#4b6b86;
  --navy-dark:#3e5c76;
  --green:#b8cf8e;
  --green-soft:#c5d9a0;
  --ink:#222;
  --body:#555;
  --footer:#2c2c2c;
  --white:#fff;
}
*{box-sizing:border-box;margin:0;padding:0}
html,body{width:1200px;height:5127px;overflow:hidden}
body{position:relative;font-family:"Lato",sans-serif;color:var(--ink);background:var(--white)}
.abs{position:absolute}
.serif{font-family:"Libre Baskerville",serif}
.script{font-family:"Allura",cursive}
.btn{position:absolute;display:flex;align-items:center;justify-content:center;border-radius:24px;font-size:13px;color:var(--white);background:var(--navy)}
.btn.green{background:var(--green);color:var(--ink)}

/* header */
.site-header{left:0;top:0;width:1200px;height:103px;border-bottom:5px solid var(--green)}
.brand{left:108px;top:22px;display:flex;align-items:center;gap:8px}
.brand-dot{width:40px;height:40px;border-radius:50%;background:var(--navy)}
.brand-name{font-family:"Libre Baskerville",serif;font-weight:700;font-size:22px;color:var(--navy)}
.brand-sub{font-size:8px;color:var(--navy);margin-top:2px}
.nav{right:88px;top:36px;display:flex;gap:24px;align-items:center;font-size:11px;color:#666}
.nav .active{background:var(--navy);color:#fff;padding:7px 16px;border-radius:16px}

/* hero */
.hero{left:0;top:105px;width:1200px;height:600px;background:linear-gradient(100deg,#5c4f40 0%,#8a6c4b 35%,#a89886 70%,#cfc9c0 100%)}
.hero-script{left:108px;top:235px;font-size:84px;color:var(--green);line-height:1}
.hero-title{left:110px;top:355px;font-size:38px;color:#fff}
.hero-text{left:110px;top:428px;width:380px;font-size:13px;line-height:26px;color:#fff}

/* services */
.kicker{font-family:"Allura",cursive;font-size:44px;color:var(--navy);text-align:center;width:1200px;left:0}
.section-title{font-family:"Libre Baskerville",serif;font-size:38px;text-align:center;width:1200px;left:0}
.service{width:236px;height:222px;top:992px;border:2px solid var(--navy);border-radius:30px;display:flex;align-items:center;justify-content:center;text-align:center;font-family:"Libre Baskerville",serif;font-size:19px;line-height:26px;padding-top:30px}
.service-icon{width:90px;height:90px;top:948px;border-radius:50%;background:var(--navy);border:4px solid #fff;box-shadow:0 0 0 2px var(--navy)}

/* video */
.video{left:0;top:1327px;width:1200px;height:630px;background:linear-gradient(90deg,#a7bd80 0%,#b6cc8c 40%,#c4d79c 100%)}
.video-script{left:588px;top:1455px;font-size:82px;color:var(--navy);line-height:1}
.video-title{left:590px;top:1570px;font-size:38px}
.video-text{left:590px;top:1640px;width:400px;font-size:12.5px;line-height:25px}

/* testimonials */
.map{left:200px;top:2095px;width:770px;height:380px;border-radius:40%;background:radial-gradient(ellipse,#eeeeee 0%,#f7f7f7 60%,#fff 100%)}
.quote{left:300px;top:2200px;width:600px;text-align:center;font-size:13.5px;line-height:31px;color:#666}
.avatar{border-radius:50%;background:#c9b8a8}

/* prices */
.prices-band{left:0;top:2677px;width:1200px;height:580px;background:linear-gradient(180deg,#4b6b86,#3f5f78)}
.price-card{top:2910px;width:234px;height:672px;background:#fff;border:2px solid var(--navy);border-radius:30px;overflow:hidden;text-align:center}
.price-head{height:54px;background:var(--green);font-family:"Libre Baskerville",serif;font-size:14px;font-weight:700;display:flex;align-items:center;justify-content:center}
.price{font-family:"Libre Baskerville",serif;font-size:21px;margin:28px 20px 0;line-height:29px;padding-bottom:16px;border-bottom:1px solid #ddd}
.features{list-style:none;margin-top:12px;font-size:10.5px;color:#666;line-height:31px;padding:0 10px}
.price-card .btn{left:36px;width:162px;height:42px;bottom:18px;background:var(--green);color:var(--ink)}

/* about */
.about-photo{left:555px;top:3692px;width:593px;height:395px;background:radial-gradient(circle at 60% 50%,#8a6a4a,#c7b49c 55%,#f4f1ec 80%)}

/* awards */
.awards{left:0;top:4210px;width:1200px;height:255px;background:var(--green-soft)}
.award{width:96px;height:96px;border-radius:50%;background:#b99a5a;top:4262px}
.award-text{top:4372px;width:260px;text-align:center;font-size:11px;line-height:20px;color:#444}

/* footer */
.footer{left:0;top:4465px;width:1200px;height:662px;background:var(--footer);color:#eee}
.foot-h{font-family:"Libre Baskerville",serif;font-size:16px;color:#fff}
.foot-list{list-style:none;font-size:11px;line-height:27.5px;color:#ddd}
</style>
</head>
<body>

<header class="abs site-header">
  <div class="abs brand">
    <span class="brand-dot"></span>
    <div><div class="brand-name">coinharborly</div><div class="brand-sub">Retirement &amp; Financial Planning Software</div></div>
  </div>
  <nav class="abs nav">
    <span class="active">HOME</span><span>HOW IT WORKS</span><span>VIDEO DEMOS</span><span>PRICES</span><span>SCREENSHOTS &amp; SAMPLE PLANS</span><span>CONTACT</span>
  </nav>
</header>

<section class="abs hero" role="img" aria-label="Person in a knit sweater typing on a laptop at a wooden desk"></section>
<div class="abs script hero-script">Planning for</div>
<h1 class="abs serif hero-title" style="font-weight:400">Financial and Retirement</h1>
<p class="abs hero-text">CoinHarborly's retirement planning and financial planning software not only gives the most accurate projections</p>
<span class="btn" style="left:108px;top:517px;width:164px;height:48px">Learn More</span>
<span class="btn green" style="left:290px;top:517px;width:166px;height:48px">Free Trial</span>

<!-- services -->
<div class="abs kicker" style="top:792px">What We Do</div>
<h2 class="abs section-title" style="top:855px;font-weight:400">Services We Offer</h2>
<div class="abs service" style="left:108px">Financial<br>Planning for<br>Everybody</div>
<div class="abs service" style="left:360px">Link Your<br>Accounts &amp; Plan<br>with Confidence</div>
<div class="abs service" style="left:612px">Run Powerful<br>Scenarios</div>
<div class="abs service" style="left:862px">Find Solutions to<br>Tough Questions</div>
<span class="abs service-icon" style="left:183px"></span>
<span class="abs service-icon" style="left:434px"></span>
<span class="abs service-icon" style="left:684px"></span>
<span class="abs service-icon" style="left:935px"></span>

<!-- video -->
<section class="abs video" role="img" aria-label="Glass jar filled with coins with a small plant growing out of it"></section>
<svg class="abs" style="left:98px;top:1414px" width="36" height="28" viewBox="0 0 36 28" fill="none" stroke="#fff" stroke-width="2"><path d="M2 8V3h32v22H22"/><path d="M2 14a12 12 0 0 1 12 12M2 20a6 6 0 0 1 6 6"/></svg>
<svg class="abs" style="left:1098px;top:1416px" width="24" height="24" stroke="#fff" stroke-width="2.5"><path d="M2 2l20 20M22 2L2 22"/></svg>
<div class="abs script video-script">Comprehensive</div>
<h2 class="abs serif video-title" style="font-weight:400">Retirement Planning</h2>
<p class="abs video-text">CoinHarborly's retirement planning and financial planning software not only gives the most accurate projections, but also</p>
<span class="btn" style="left:588px;top:1728px;width:164px;height:46px">Learn More</span>
<svg class="abs" style="left:88px;top:1847px" width="1050" height="52"><circle cx="26" cy="26" r="26" fill="#fff"/><path d="M20 15l16 11-16 11z" fill="var(--navy)"/><line x1="62" y1="26" x2="950" y2="26" stroke="#fff" stroke-opacity=".6" stroke-width="2"/></svg>
<div class="abs" style="left:1053px;top:1862px;color:#fff;font-size:19px">2:05:49</div>

<!-- testimonials -->
<div class="abs map" role="img" aria-label="Faint dotted world map"></div>
<h2 class="abs section-title" style="top:2098px">Testimonials</h2>
<p class="abs quote">"This product is exactly as advertised. It is easy to set up and use, gives excellent data and makes running various scenarios simple. It is way more versatile and accurate than free programs available on-line. I'm delighted with my purchase."</p>
<svg class="abs" style="left:148px;top:2270px" width="20" height="30" fill="none" stroke="#333" stroke-width="2"><path d="M16 2L4 15l12 13"/></svg>
<svg class="abs" style="left:1048px;top:2270px" width="20" height="30" fill="none" stroke="#333" stroke-width="2"><path d="M4 2l12 13L4 28"/></svg>
<span class="abs avatar" style="left:486px;top:2380px;width:56px;height:56px;background:#b9b0a6" role="img" aria-label="Customer portrait"></span>
<span class="abs avatar" style="left:670px;top:2380px;width:56px;height:56px;background:#c7b6aa" role="img" aria-label="Customer portrait"></span>
<span class="abs avatar" style="left:540px;top:2337px;width:134px;height:134px;border:5px solid var(--navy);background:#c4a58c" role="img" aria-label="Portrait of the reviewer"></span>
<div class="abs script" style="left:0;width:1200px;text-align:center;top:2505px;font-size:40px">Dana Whitlock</div>

<!-- prices -->
<section class="abs prices-band" role="img" aria-label="Dimmed photo of people walking outdoors under trees"></section>
<div class="abs kicker" style="top:2718px;color:#fff">Prices</div>
<h2 class="abs section-title" style="top:2792px;color:#fff;font-weight:400">What We Offer</h2>

<div class="abs price-card" style="left:110px">
  <div class="price-head">Individuals: Basic</div>
  <div class="price">$189 Per Year</div>
  <ul class="features"><li>Unlimited Use</li><li>Email Support</li><li>Live Chat Support</li></ul>
  <span class="btn">Get Started</span>
</div>
<div class="abs price-card" style="left:362px">
  <div class="price-head">Individuals: Advanced</div>
  <div class="price">$229 Per Year</div>
  <ul class="features"><li>Unlimited Use</li><li>Email Support</li><li>Live Chat Support</li><li>Access Expert One On One</li><li>Support*</li><li>Monte Carlo Analysis</li><li>What-If Scenarios</li><li>Link Your Investment Accounts</li><li>*Add on charge applies.</li></ul>
  <span class="btn">Get Started</span>
</div>
<div class="abs price-card" style="left:614px">
  <div class="price-head">Individuals: Deluxe</div>
  <div class="price">$289 Per Year</div>
  <ul class="features"><li>Unlimited Use</li><li>Email &amp; Phone Support</li><li>Live Chat Support</li><li>Access Expert One On One</li><li>Support*</li><li>Monte Carlo Analysis</li><li>What-If Scenarios</li><li>Link Your Investment Accounts</li><li>Historical Data For Investments</li><li>Performance History</li><li>View Your Fund Fees</li><li>Roth Conversion Scenarios</li><li>Asset Allocation Scenarios</li><li>Federal Income Tax Scenarios</li><li>*Add on charge applies.</li></ul>
  <span class="btn">Get Started</span>
</div>
<div class="abs price-card" style="left:864px">
  <div class="price-head">Advisor</div>
  <div class="price">$899 Per Year<br>Or $275 Per<br>Quarter</div>
  <ul class="features"><li>Email &amp; Phone Support</li><li>Client Portal</li><li>Online Fact Finder</li><li>Model Portfolios</li><li>Customized Reports</li><li>Monte Carlo Analysis</li><li>Link Client Accounts Using</li><li>Accountlink*</li><li>What-If Scenarios</li><li>Asset Allocation Scenarios</li><li>Roth Conversion Scenarios</li><li>*Add on charge applies.</li></ul>
  <span class="btn">Get Started</span>
</div>

<!-- about -->
<div class="abs script" style="left:118px;top:3740px;font-size:44px;color:var(--navy)">About Us</div>
<h2 class="abs serif" style="left:118px;top:3810px;font-size:38px;font-weight:400">Who We Are</h2>
<p class="abs" style="left:118px;top:3885px;width:470px;font-size:12.5px;line-height:26px;color:var(--body)">CoinHarborly has the power and accuracy that advisors demand, but with an interface that consumers can enjoy. Advisor Financial Planning and Personal Financial Planning Software: Flexible, interactive, financial and retirement planning software for everybody.</p>
<span class="btn" style="left:118px;top:4030px;width:186px;height:48px">Screens and Plans</span>
<div class="abs about-photo" role="img" aria-label="Leather wallet with coins under a magnifying glass"></div>

<!-- awards -->
<section class="abs awards"></section>
<span class="abs award" style="left:252px"></span>
<span class="abs award" style="left:567px"></span>
<span class="abs award" style="left:880px"></span>
<div class="abs award-text" style="left:170px">Ranked in Ledgerpoint's "Best Financial Planning Software Programs"</div>
<div class="abs award-text" style="left:485px">Voted Best Retirement Planning Software by PlannerDesk</div>
<div class="abs award-text" style="left:798px">Most Comprehensive Financial Planning Software: Finwire Daily</div>

<!-- footer -->
<footer class="abs footer">
  <div class="abs brand" style="left:136px;top:48px">
    <span class="brand-dot" style="background:#fff"></span>
    <div><div class="brand-name" style="color:#fff">coinharborly</div><div class="brand-sub" style="color:#ddd">Retirement &amp; Financial Planning Software</div></div>
  </div>
  <p class="abs" style="left:500px;top:46px;width:520px;font-size:11px;line-height:21px;color:#ddd">CoinHarborly has the power and accuracy that advisors demand, but with an interface that consumers can enjoy. Advisor Financial Planning and Personal Financial Planning Software: Flexible, interactive, financial and retirement planning software for everybody.</p>
  <div class="abs" style="left:122px;top:218px;width:956px;border-top:1px solid #444"></div>
  <div class="abs foot-h" style="left:122px;top:297px">Social Media</div>
  <div class="abs" style="left:124px;top:350px;display:flex;gap:14px">
    <span style="width:12px;height:12px;border-radius:50%;background:#fff"></span><span style="width:12px;height:12px;border-radius:50%;background:#fff"></span><span style="width:12px;height:12px;border-radius:50%;background:#fff"></span><span style="width:12px;height:12px;border-radius:50%;background:#fff"></span>
  </div>
  <div class="abs" style="left:122px;top:392px;font-size:11px">Copyright © 2022 CoinHarborly</div>
  <div class="abs foot-h" style="left:430px;top:297px">Important Links</div>
  <ul class="abs foot-list" style="left:430px;top:345px"><li>FAQ</li><li>Press</li><li>Security &amp; Privacy</li><li>Video Demos</li><li>Expert Planning Help</li><li>Advisor Webinar</li><li>Advisor Client Login</li></ul>
  <ul class="abs foot-list" style="left:620px;top:345px"><li>Screenshots</li><li>Financial Calculators</li><li>Questionnaires</li><li>Blog</li><li>User Guide</li><li>Site Map</li></ul>
  <div class="abs foot-h" style="left:850px;top:297px">Contact Us</div>
  <svg class="abs" style="left:856px;top:352px" width="16" height="16" fill="#fff"><path d="M3 1l3 3-2 2c1 2 3 4 5 5l2-2 3 3-2 3C6 15 1 10 0 3z"/></svg>
  <div class="abs" style="left:884px;top:352px;font-size:11px">+1-800-555-0147</div>
  <svg class="abs" style="left:856px;top:400px" width="16" height="12" fill="none" stroke="#fff" stroke-width="1.5"><rect x="1" y="1" width="14" height="10"/><path d="M1 1l7 6 7-6"/></svg>
  <div class="abs" style="left:884px;top:398px;font-size:11px;line-height:23px">sales@coinharborly.com<br>support@coinharborly.com</div>
</footer>

</body>
</html>
```